Lantern Forge needs a business card

The logo we have uploaded is going to be the image centered on the back.
The business card color is going to be black. Increase the contrast in the logo and lettering so the grey stands out from the black and is more readable. Keep the shadow effect if you can.
On the front, the only part of the logo that should be used is the Egyptian character. We would like the following information included: Name (first last), Title, Phone number, email and company name (Lantern Forge).
The images of colored sound waves we uploaded is a concept we would like implemented on the front as well but please do not use the exact image. It is for guideline purposes.
Get creative with the empty space. We are a technology company that deals with sound and lights. Please not too busy.
Thank you, we look forward to all your submissions.

```html
<!DOCTYPE html>
<html lang="en">
<head>
<meta charset="utf-8">
<title>Lantern Forge – Business Card</title>
<link href="https://fonts.googleapis.com/css2?family=Lato:wght@400;700&display=swap" rel="stylesheet">
<style>
  :root {
    --backdrop: #2b2624;
    --card: #0b0b0b;
    --card-edge: #161616;
    --accent: #e0282e;
    --steel: #7c8a90;
    --text-soft: #b9bec1;
    --mark-light: #8a8a8a;
    --divider: #1c1c1c;
  }
  * { margin: 0; padding: 0; box-sizing: border-box; }
  html, body {
    width: 1200px; height: 844px; overflow: hidden;
    background: var(--backdrop);
    font-family: "Lato", Arial, sans-serif;
  }
  .stage {
    position: relative; width: 1200px; height: 844px;
    display: flex; align-items: center; justify-content: center; gap: 60px;
  }
  .card {
    width: 500px; height: 286px;
    background: var(--card);
    border: 1px solid var(--card-edge);
    box-shadow: 0 12px 30px rgba(0,0,0,.55);
    position: relative;
  }
  /* front */
  .card--front { display: flex; }
  .front__brand {
    width: 50%; display: flex; align-items: center; justify-content: center; gap: 10px;
  }
  .front__divider {
    width: 1px; background: var(--divider); margin: 0;
  }
  .brand-square {
    width: 14px; height: 14px; background: var(--accent);
  }
  .brand-name {
    font-weight: 700; font-size: 26px; letter-spacing: 1px;
    color: var(--steel); text-transform: uppercase;
  }
  .front__details {
    width: 50%; padding: 44px 0 0 22px; color: var(--text-soft);
    font-size: 13.5px; line-height: 1.35;
  }
  .person-name { color: var(--accent); font-size: 19px; font-weight: 700; }
  .person-title { margin-bottom: 14px; }
  .address { margin-bottom: 14px; }
  .contact-label { color: var(--accent); display: inline-block; width: 16px; }
  /* back */
  .card--back {
    display: flex; flex-direction: column; align-items: center; justify-content: center; gap: 8px;
  }
  .back__brand { display: flex; align-items: center; gap: 12px; }
  .back__brand .brand-square { width: 18px; height: 18px; background: var(--mark-light); }
  .back__brand .brand-name {
    font-size: 34px; color: var(--mark-light);
  }
</style>
</head>
<body>
  <main class="stage">
    <section class="card card--front" aria-label="Business card front">
      <div class="front__brand">
        <span class="brand-square"></span>
        <span class="brand-name">Lantern Forge</span>
      </div>
      <div class="front__divider"></div>
      <div class="front__details">
        <p class="person-name">Marcus Hale</p>
        <p class="person-title">Managing Director</p>
        <p class="address">12345, Address Goes Here<br>Country Name, 123456.</p>
        <p><span class="contact-label">T:</span> 044-987 654 321</p>
        <p><span class="contact-label">E:</span> hello@lanternforge.example</p>
        <p><span class="contact-label">W:</span>www.lanternforge.example</p>
      </div>
    </section>
    <section class="card card--back" aria-label="Business card back">
      <div class="back__brand">
        <span class="brand-square"></span>
        <span class="brand-name">Lantern Forge</span>
      </div>
    </section>
  </main>
</body>
</html>
```